Brenmoor Group needs a business card

I would like the card to be simple but modern and elegant.
I like black and white.
or black and gold.
we are a private finance lender and also are involved in property and property developments.

please look at the business card photos i provided i would like B.G only one one side and all the other details on the other side use fonts that tie in with my theme.

Industry/Entity Type

Finance

Contact Information for Business Card

Brenmoor Group (B.G) Callum Brenmoor M: 0418396152 E: callumbren@quivomail.com

Font styles to use
Other font styles liked:
• Use fonts that would reflect our business

Colors
000000
ffffff

Requirements
Must have
• one side of details
• other side has either B.G or Brenmoor Group like in the photos provided

```html
<!DOCTYPE html>
<html lang="en">
<head>
<meta charset="utf-8">
<title>Brenmoor Group — Business Card</title>
<link href="https://fonts.googleapis.com/css2?family=Sorts+Mill+Goudy&display=swap" rel="stylesheet">
<style>
  :root {
    --paper: #ffffff;
    --card: #030303;
    --gold: #857650;
    --serif: "Sorts Mill Goudy", "Goudy Old Style", Georgia, serif;
  }
  html, body {
    margin: 0;
    padding: 0;
    width: 960px;
    height: 1200px;
    overflow: hidden;
    background: var(--paper);
  }
  .sheet {
    position: relative;
    width: 960px;
    height: 1200px;
    font-family: var(--serif);
    color: var(--gold);
  }
  .card {
    position: absolute;
    width: 840px;
    height: 480px;
    background: var(--card);
  }
  .card--front { left: 54px; top: 83px; }
  .card--back  { left: 58px; top: 633px; }

  .frame {
    position: absolute;
    left: 14px;
    top: 16px;
    right: 14px;
    bottom: 14px;
    border: 7px double var(--gold);
  }

  /* Front */
  .panel {
    position: absolute;
    left: 100px;
    top: 72px;
    width: 637px;
    height: 334px;
    border: 1.5px solid var(--gold);
  }
  .mark-dot {
    position: absolute;
    left: 379px;
    top: 123px;
    width: 80px;
    height: 80px;
    border-radius: 50%;
    background: var(--gold);
  }
  .wordmark {
    position: absolute;
    left: 0;
    top: 210px;
    width: 840px;
    text-align: center;
    font-size: 38px;
    letter-spacing: 0.5px;
    line-height: 1;
    text-transform: uppercase;
  }
  .rule-pair {
    position: absolute;
    top: 235px;
    width: 112px;
    height: 9px;
    border-top: 2px solid var(--gold);
    border-bottom: 2px solid var(--gold);
    box-sizing: border-box;
  }
  .rule-pair--left  { left: 100px; }
  .rule-pair--right { left: 626px; }

  /* Back */
  .contact-name {
    position: absolute;
    left: 40px;
    top: 156px;
    margin: 0;
    padding: 0 4px 6px 4px;
    font-size: 40px;
    font-weight: 400;
    line-height: 1;
    border-bottom: 3px solid var(--gold);
  }
  .contact-line {
    position: absolute;
    margin: 0;
    font-size: 34px;
    line-height: 1;
  }
  .contact-line--mobile { left: 44px; top: 253px; }
  .contact-line--email  { left: 48px; top: 310px; font-size: 33px; }
  .mark-dot--back {
    left: 634px;
    top: 169px;
    width: 128px;
    height: 128px;
  }
</style>
</head>
<body>
<main class="sheet">
  <section class="card card--front" aria-label="Card front">
    <div class="frame"></div>
    <div class="panel"></div>
    <div class="mark-dot"></div>
    <span class="rule-pair rule-pair--left"></span>
    <h1 class="wordmark" style="margin:0;font-weight:400;">Brenmoor Group</h1>
    <span class="rule-pair rule-pair--right"></span>
  </section>

  <section class="card card--back" aria-label="Card back">
    <div class="frame"></div>
    <h2 class="contact-name">Callum Brenmoor</h2>
    <p class="contact-line contact-line--mobile">M: 0418396152</p>
    <p class="contact-line contact-line--email">E: callumbren@quivomail.com</p>
    <div class="mark-dot mark-dot--back"></div>
  </section>
</main>
</body>
</html>
```